Exciting New Reseller Brand requires Website to WOW New clients to register.

We are a NEW online business called Trade Our Goods.

The Website is a simple concept, it looks to put Merchants (businesses that want their products resold) in touch with Resellers (people or businesses that want to resell that product).

The website acts as an online market place which looks to get Merchants to sign-up and pay to list their company and product as well as getting Resellers to sign-up to view potential Merchants they can get in touch with in the right industry or area to resell their products for (see attached slide-pack to explain packages)

Any type of Industry or Business can register themselves to get listed on Trade Our Goods to see either get their product/service resold or to look for products / services to reseller.

Trade Our Goods does not take any other monetary part in the business relationships other than to obtain money for the monthly website subscription.

We want a very simple website, so this project is for several pages:

Page 1) A really vibrant, exciting, image based homepage to get people to sign-up / register (see sites that we like in the project brief). Needs to be very clear that there are 2 customers and to sign up to join, build and earn!

Page 2) A page that describes the benefits and packages for Resellers.

Page 3) A page that describes the benefits and packages for Merchants.

Page 4) The Payment process pages, taking the customer through sign-up

Page 5) The Business Listings page, so when people search for a Merchant how this will be displayed.

We would really like an image based site and preferably parallax. We want it bright vibrant and to look like a social media site.

All necessary files / logos enclosed.

We would love to continue to work with the winning designer moving forward.

Many thanks and Good Luck.

Regards

Martin & Owen

Target Market(s)

Merchants, Suppliers, Vendors, Manufacturers, Distributors, Wholesalers, Affiliate programs, Franchisees, Reselers

Industry/Entity Type

Business

Number of Pages Required

5+ page

Requirements
Must have
• We love the following websites:
• 1) Like the top section, i.e. parallax image based: www.brightkitestudio.co.uk
• 2) Like the way the screen is split in 2, could be used to describe the 2 different customers we are after Merchants / Resellers: www.filevault-example.com/guide
• 3) Like the bright colours / full screen video split into 2 below top banner and the generally how simple the site is: www.harbourlinden.com.au
• 4) Love all of this site, simple, bold, Love the colours, the clear message and the infographics: http://www.velorin-example.com/swiftrider/faster

```html
<!DOCTYPE html>
<html lang="en">
<head>
<meta charset="utf-8">
<title>Trade Our Goods — Join, Build, Earn</title>
<link rel="stylesheet" href="https://fonts.googleapis.com/css2?family=Open+Sans:wght@300;400&family=Raleway:wght@400;500;600;700&display=swap">
<style>
  :root {
    --ink: #222;
    --body-text: #333;
    --nav-text: #6b6b6b;
    --rule: #a9a9a9;
    --brand-green: #9bc43a;
    --brand-blue: #0a8fd0;
    --merchant-tone-a: #a9c06d;
    --merchant-tone-b: #6f8d45;
    --reseller-tone-a: #82c6e6;
    --reseller-tone-b: #1f6f98;
    --white: #fff;
    --field-border: #555;
    --go-button: #c2c2c2;
  }
  * { box-sizing: border-box; margin: 0; padding: 0; }
  html, body { width: 1200px; height: 882px; overflow: hidden; background: var(--white); }
  body { position: relative; font-family: "Open Sans", sans-serif; color: var(--ink); }

  .site-header { position: absolute; top: 0; left: 0; width: 1200px; height: 152px; }
  .brand {
    position: absolute; left: 0; width: 1200px; top: 42px;
    display: flex; justify-content: center; align-items: center; gap: 12px;
    font-family: "Raleway", sans-serif; font-weight: 700; font-size: 34px; color: var(--brand-green);
  }
  .brand-dot { width: 40px; height: 40px; border-radius: 50%; background: var(--brand-blue); }

  .account-login { position: absolute; left: 885px; top: 28px; width: 270px; }
  .account-login__label { font-size: 13px; margin-left: 7px; display: block; margin-bottom: 6px; line-height: 16px; }
  .account-login__row { display: flex; align-items: center; }
  .account-login__field {
    height: 25px; border: 1px solid var(--field-border); border-radius: 7px;
    font-family: "Raleway", sans-serif; font-size: 10px; padding: 0 5px; line-height: 23px;
    color: var(--ink); white-space: nowrap; overflow: hidden;
  }
  .account-login__field--user { width: 113px; }
  .account-login__field--pass { width: 113px; margin-left: 10px; }
  .account-login__go {
    width: 25px; height: 25px; border-radius: 50%; background: var(--go-button);
    margin-left: 6px; display: flex; align-items: center; justify-content: center;
  }

  .main-nav {
    position: absolute; top: 127px; left: 0; width: 1200px;
    display: flex; justify-content: center; align-items: center;
    font-weight: 300; font-size: 14px; color: var(--nav-text); white-space: nowrap;
  }
  .main-nav .sep { margin: 0 11px; }
  .main-nav .sep--tight { margin: 0 6px; }
  .main-nav--rule { position: absolute; top: 151px; left: 0; width: 1200px; height: 2px; background: var(--rule); }

  .hero { position: absolute; top: 153px; left: 0; width: 1200px; height: 406px; display: flex; }
  .hero-panel { position: relative; width: 600px; height: 406px; }
  .hero-panel--merchant { background: radial-gradient(circle at 280px 240px, #b8d77a 0, var(--merchant-tone-a) 30%, var(--merchant-tone-b) 100%); }
  .hero-panel--reseller { background: linear-gradient(160deg, var(--reseller-tone-b) 0%, #3f93bd 40%, var(--reseller-tone-a) 100%); }
  .register-cta { position: absolute; width: 196px; text-align: center; font-family: "Raleway", sans-serif; color: var(--white); }
  .register-cta__lead { font-weight: 700; font-size: 32px; line-height: 1; margin-bottom: 8px; white-space: nowrap; margin-left: -40px; margin-right: -40px; }
  .register-cta__box {
    height: 63px; border: 5px solid var(--white); border-radius: 8px;
    font-weight: 600; font-size: 32px; line-height: 53px; white-space: nowrap;
  }
  .hero-panel--merchant .register-cta { left: 256px; top: 261px; }
  .hero-panel--merchant .register-cta__box { background: rgba(70, 100, 50, 0.55); }
  .hero-panel--reseller .register-cta { left: 158px; top: 256px; }
  .hero-panel--reseller .register-cta__box { background: rgba(120, 195, 232, 0.6); }

  .intro { position: absolute; top: 598px; left: 143px; width: 918px; font-size: 13px; line-height: 16px; letter-spacing: -0.15px; color: var(--body-text); text-align: justify; }
  .intro p + p { margin-top: 16px; }

  .site-footer { position: absolute; top: 774px; left: 0; width: 1200px; text-align: center; font-family: "Raleway", sans-serif; font-size: 11px; color: var(--ink); }
  .site-footer__rule { width: 316px; height: 1px; background: var(--rule); margin: 0 auto; }
  .footer-nav { margin-top: 40px; display: flex; justify-content: center; white-space: nowrap; }
  .footer-nav .sep { margin: 0 9px; }
  .footer-nav .sep--tight { margin: 0 4px; }
  .copyright { margin-top: 14px; }
</style>
</head>
<body>
  <header class="site-header">
    <div class="brand"><span class="brand-dot"></span><span>Trade Our Goods</span></div>

    <form class="account-login" aria-label="Account login">
      <span class="account-login__label">Account login:</span>
      <div class="account-login__row">
        <span class="account-login__field account-login__field--user">ENTER USERNAME</span>
        <span class="account-login__field account-login__field--pass">PASS</span>
        <span class="account-login__go">
          <svg width="12" height="12" viewBox="0 0 12 12"><polygon points="2,1 11,6 2,11" fill="#fff"/></svg>
        </span>
      </div>
    </form>

    <nav class="main-nav">
      <span>HOME</span><span class="sep">|</span>
      <span>ABOUT US</span><span class="sep">|</span>
      <span>FOR MERCHANTS</span><span class="sep">|</span>
      <span>FOR RESELLERS</span><span class="sep sep--tight">|</span>
      <span>PAYMENT</span><span class="sep">|</span>
      <span>LISTINGS</span><span class="sep">|</span>
      <span>CONTACTS</span>
    </nav>
    <div class="main-nav--rule"></div>
  </header>

  <section class="hero">
    <div class="hero-panel hero-panel--merchant" role="img" aria-label="Photo of a businessman pressing a glowing button, tinted green">
      <div class="register-cta">
        <div class="register-cta__lead">Register as</div>
        <div class="register-cta__box">MERCHANT</div>
      </div>
    </div>
    <div class="hero-panel hero-panel--reseller" role="img" aria-label="Photo of a laptop keyboard, tinted blue">
      <div class="register-cta">
        <div class="register-cta__lead">Register as</div>
        <div class="register-cta__box">RESELLER</div>
      </div>
    </div>
  </section>

  <main class="intro">
    <p>Vestibulum ante ipsum primis in faucibus orci luctus et ultrices posuere cubilia Curae; Integer consectetur ac magna in gravida. Integer ut enim. Donec eget commodo est, porttitor Vestibulum ante ipsum primis in faucibus orci luctus et ultrices posuere cubilia Curae; Integer consectetur ac magna in gravida. Integer ut ur na enim. Donec eget commodo est, porttitor Vestibulum ante ipsum primis in faucibus orci luctus et ultrices posuere cubilia Curae; Integer consectetur ac magna in gravida. Integer ut urna enim.</p>
    <p>Curae; Integer consectetur ac magna in gravida. Integer ut enim. Donec eget commodo est, porttitor Vestibulum ante ipsum primis in faucibus orci luctus et ultrices posuere cubilia Curae; Integer consectetur ac magna in gravida. Integer ut ur na enim. Donec eget commodo est, porttitor Vestibulum ante ipsum primis in faucibus orci luctus et ultrices posuere cubilia Curae; Integer consectetur ac magna in gravida. Integer ut urna enim.</p>
  </main>

  <footer class="site-footer">
    <div class="site-footer__rule"></div>
    <nav class="footer-nav">
      <span>HOME</span><span class="sep">|</span>
      <span>ABOUT US</span><span class="sep">|</span>
      <span>FOR MERCHANTS</span><span class="sep">|</span>
      <span>FOR RESELLERS</span><span class="sep sep--tight">|</span>
      <span>PAYMENT</span><span class="sep">|</span>
      <span>LISTINGS</span><span class="sep">|</span>
      <span>CONTACTS</span>
    </nav>
    <p class="copyright">Copyright Trade Our Goods © 2015</p>
  </footer>
</body>
</html>
```